Rex Tollbridge (Burn The Stack) CD Cover Design

Professional Cd cover design needed. No photo of the artist necessary for this cover. You can search Rex Tollbridge on YouTube for a feel of the artist, inspiration, etc. Song (Burn The Stack)!

Target Market(s)

Big money makers , Hustlers, those who don't mind spending cash.

Colors

Designer to choose colors to be used in the design.

Requirements
Nice to have
• Any symbols related to money.

```html
<!DOCTYPE html>
<html lang="en">
<head>
<meta charset="utf-8">
<title>Rex Tollbridge – Burn The Stack</title>
<link rel="stylesheet" href="https://fonts.googleapis.com/css2?family=Great+Vibes&family=Stardos+Stencil:wght@700&family=Abril+Fatface&display=swap">
<style>
  :root {
    --red-top: #ff0a0a;
    --red-bottom: #b30000;
    --ink: #000000;
    --ink-soft: #141414;
    --paper: #ffffff;
    --stencil: #d9d4d0;
    --frame: #3a3a3a;
  }
  html, body {
    margin: 0;
    padding: 0;
    overflow: hidden;
    background: var(--paper);
  }
  .cover {
    position: relative;
    width: 1200px;
    height: 1200px;
    box-sizing: border-box;
    border: 4px solid var(--frame);
    background: linear-gradient(180deg, var(--red-top) 0%, var(--red-bottom) 100%);
    overflow: hidden;
  }
  .artwork-area {
    position: absolute;
    left: 0;
    top: 0;
    width: 1200px;
    height: 1200px;
  }
  .title {
    position: absolute;
    margin: 0;
    font-family: "Great Vibes", cursive;
    font-weight: 400;
    color: var(--paper);
    line-height: 1;
    white-space: nowrap;
  }
  .title-line-one {
    left: 185px;
    top: 330px;
    font-size: 230px;
  }
  .title-line-two {
    left: 135px;
    top: 545px;
    font-size: 205px;
  }
  .dollar-mark {
    position: absolute;
    left: 770px;
    top: 330px;
    font-family: "Abril Fatface", serif;
    font-size: 440px;
    line-height: 1;
    color: var(--ink);
    transform: rotate(-6deg);
  }
  .artist-name {
    position: absolute;
    right: 72px;
    top: 1018px;
    margin: 0;
    font-family: "Stardos Stencil", sans-serif;
    font-weight: 700;
    font-size: 68px;
    letter-spacing: 2px;
    color: var(--stencil);
    text-transform: uppercase;
    white-space: nowrap;
  }
</style>
</head>
<body>
  <div class="cover">
    <svg class="artwork-area" viewBox="0 0 1200 1200" role="img" aria-label="Dark silhouette illustration sweeping diagonally behind the title">
      <defs>
        <linearGradient id="artwork-fill" x1="0" y1="0" x2="0" y2="1">
          <stop offset="0" stop-color="var(--ink-soft)"/>
          <stop offset="1" stop-color="var(--ink)"/>
        </linearGradient>
      </defs>
      <rect x="230" y="60" width="480" height="1060" rx="60" fill="url(#artwork-fill)" transform="rotate(20 470 590)"/>
    </svg>
    <h1 class="title title-line-one">Burn</h1>
    <p class="title title-line-two">the stack</p>
    <span class="dollar-mark">$</span>
    <p class="artist-name">Rex Tollbridge</p>
  </div>
</body>
</html>
```